EPC Marketing Flyer TH Tidewell

Company Name: Tidewell Housing Ltd
Product: Residential EPCs
Territory: Nationwide (UK)
Marketing channel: Flyer will be used for email and postal mailshots. We have not targeted this particular segment of the market before, so we need it to be eye catching, clearly messaged and encourage the recipient to get in touch.

We need a flyer to promote our services to conduct EPCs owned by public and private sector for residential ONLY (NOT Commercial), on a large or small scale.

Our Surveyors: experienced and accredited surveyors, quality service, quick and professional

Our Business: Warm Path Accredited, Reputation in business for excellence, fast growing

Our Service: Friendly, high quality, quick and professional

Colours: Designs in green and white (same shade as corporate colours), with our logo, and warm path accreditation logo, promoting our business.

Target Market(s)

Estate Agencies, Housing Associations, Local Authorities (Housing Departments), House Builders (NOT Home Owners Directly)

Industry/Entity Type

It Company

Font styles to use
Sans Serif
Other font styles liked:
• Calibri

Colors
add136
9bcb3c
cadf82
f6faec
eaf2ce

Requirements
Must have
• Our contact number etc must be clearly visible, and that we do EPCs
• Must state: What is an EPC? An EPC (Energy Performance Certificate) gives a property an energy efficiency rating from A (most efficient) to G (least efficient) and is valid for 10 years. An EPC can also provide recommendations on home improvement measures which once complete can improve the energy efficiency of the property.
• Who needs and EPC? All landlords and home owners, as all properties available to buy or rent require a valid and current EPC.
• Contact details:
• Tel: 08000 614 905
• Website: www.th-tidewell.co.uk
• Email: epc@th-tidewell.co.uk
• we must also be ably to print out the flyer
Nice to have
• Nice images to accompany the text which give a feeling of Environmentally Green, Home Energy Efficiency, Home Warmth and family - see example attached. And image of survey professional at work.
Should not have
• Any reference to cost or pricing
• Warm path logo art work must not be any other size that that specified in guidance document attached.

```html
<!DOCTYPE html>
<html lang="en">
<head>
<meta charset="utf-8">
<title>EPC Flyer – Tidewell Housing Ltd</title>
<link href="https://fonts.googleapis.com/css2?family=PT+Sans:ital,wght@0,400;0,700;1,400&display=swap" rel="stylesheet">
<style>
  :root{
    --green:#5ab446;
    --green-deep:#3e8f3a;
    --green-band:#3f8e3c;
    --lime:#9bcb3c;
    --lime-soft:#cadf82;
    --ink:#161616;
    --bar-dark:#1d1414;
    --stage:#ecece8;
    --white:#ffffff;
    --roof:#f0a62a;
    --paper:#eef1f4;
    --plan-blue:#2f7fc4;
  }
  *{margin:0;padding:0;box-sizing:border-box}
  html,body{width:1200px;height:857px;overflow:hidden;background:var(--stage)}
  body{font-family:"PT Sans",sans-serif;position:relative}
  .flyer{position:absolute;left:311px;top:20px;width:578px;height:817px;overflow:hidden;background:var(--white);box-shadow:0 4px 14px rgba(0,0,0,.25)}
  .top-bar{position:absolute;left:0;top:0;width:100%;height:20px;background:var(--bar-dark)}
  .top-bar__accent{position:absolute;left:0;top:0;width:282px;height:100%;background:var(--lime)}
  .hero-sky{position:absolute;left:0;top:20px;width:100%;height:492px;
    background:linear-gradient(180deg,#9fb0c4 0%,#d7dde6 30%,#c2c6cd 55%,#eef0f2 80%,#f6f7f6 100%)}
  .hero-art{position:absolute;left:0;top:148px;width:300px;height:370px;border-radius:0 40px 40px 0;
    background:
      radial-gradient(ellipse 46% 34% at 48% 36%,rgba(240,166,42,.95) 0%,rgba(240,166,42,.75) 55%,rgba(240,166,42,0) 100%),
      linear-gradient(160deg,#b9c4d2 0%,var(--paper) 45%,#dfe6ee 70%,var(--plan-blue) 100%)}
  .brand{position:absolute;left:44px;top:58px;display:flex;align-items:center;gap:10px}
  .brand__dot{width:56px;height:56px;border-radius:50%;background:var(--green)}
  .brand__name{font-size:21px;font-weight:700;color:var(--ink);line-height:1.05;width:130px}
  .tagline{position:absolute;left:313px;top:78px;font-size:12.5px;font-style:italic;color:#333;line-height:16px}
  .tagline em{color:var(--green-deep);font-style:italic}
  .promise{position:absolute;left:289px;top:180px;width:314px;height:314px;border-radius:50%;background:var(--green)}
  .promise__head{position:absolute;left:348px;top:210px;font-size:38px;font-weight:700;color:var(--white);line-height:47px;white-space:nowrap}
  .promise__sub{position:absolute;left:350px;top:396px;font-size:18px;font-weight:700;color:var(--ink);line-height:21px}
  .grass-art{position:absolute;left:0;top:512px;width:100%;height:215px;
    background:linear-gradient(180deg,#9fd05a 0%,#7cc23c 40%,#5faa2e 100%)}
  .info{position:absolute;left:24px;top:520px;width:516px;color:var(--ink)}
  .info h2{font-weight:700;line-height:1}
  .info h2 .big{font-size:41px}
  .info h2 .small{font-size:15px}
  .info p{font-size:15px;line-height:16px}
  .info .who{margin-top:14px}
  .info .who .big{font-size:21px}
  .rule{position:absolute;left:0;top:727px;width:100%;height:5px;background:#2a2a24}
  .contact{position:absolute;left:0;top:732px;width:100%;height:85px;background:var(--green-band);text-align:center}
  .contact__line{margin-top:6px;color:var(--lime);font-size:26px;white-space:nowrap}
  .contact__line strong{font-weight:700}
  .contact__line .mail{font-size:16px}
  .contact__web{margin-top:6px;color:var(--white);font-size:13px;letter-spacing:5px}
</style>
</head>
<body>
  <div class="flyer">
    <div class="top-bar"><div class="top-bar__accent"></div></div>
    <div class="hero-sky" role="img" aria-label="Misty sky over distant mountains"></div>
    <div class="hero-art" role="img" aria-label="Illustration of a house with orange roofs seen through a magnifying glass, standing on building plans"></div>

    <div class="brand">
      <div class="brand__dot"></div>
      <div class="brand__name">Tidewell Housing Ltd</div>
    </div>
    <p class="tagline"><em>Warm Path Accredited</em>, Reputation<br>in business for excellence, fast growing</p>

    <div class="promise"></div>
    <h1 class="promise__head">Friendly,<br>High Quality,<br>Quick and<br>Professional</h1>
    <p class="promise__sub">EXPERIENCED AND<br>ACCREDITED<br>SURVEYORS</p>

    <div class="grass-art" role="img" aria-label="Photograph of green grass field"></div>
    <section class="info">
      <h2><span class="big">What is</span> <span class="small">an EPC?</span></h2>
      <p>An EPC (Energy Performance Certificate)<br>gives a property an energy efficiency rating from A (most efficient) to G (least efficient) and is valid for 10 years. An EPC can also provide recommendations on home improvement measures which once complete can improve the energy efficiency of the property.</p>
      <h2 class="who"><span class="big">Who needs</span> <span class="small">and EPC?</span></h2>
      <p>All landlords and home owners,<br>as all properties available to buy or rent require a valid and current EPC.</p>
    </section>

    <div class="rule"></div>
    <footer class="contact">
      <p class="contact__line">Call Us &nbsp;<strong>08000 614 905</strong> or <span class="mail">epc@th-tidewell.co.uk</span></p>
      <p class="contact__web">www.th-tidewell.co.uk</p>
    </footer>
  </div>
</body>
</html>
```